Product Line Brochure

Would like to have a bifold brochure for our product line to show to customers. Would like it to incorporate the paragraph description of the product line with the picture, followed by the product listings. I would like the brochure to be clean and modern. We are a specialty chemical manufacturer in NJ area.

```html
<!DOCTYPE html>
<html lang="en">
<head>
<meta charset="utf-8">
<title>Northgate Polymer, Inc. — Product Line Brochure</title>
<link rel="stylesheet" href="https://fonts.googleapis.com/css2?family=Montserrat:wght@400;600;800&display=swap">
<style>
  :root {
    --navy: #1f3a63;
    --navy-deep: #142a4a;
    --glass-light: #5fa6dd;
    --glass-mid: #1f6aa5;
    --glass-dark: #123a63;
    --accent-red: #d8262e;
    --accent-blue: #2f6fd0;
    --paper: #ffffff;
    --ink: #3b3f46;
    --backdrop: #e9eaec;
  }
  * { box-sizing: border-box; margin: 0; padding: 0; }
  html, body { width: 1200px; height: 832px; overflow: hidden; }
  body {
    background: var(--backdrop);
    font-family: "Montserrat", Arial, sans-serif;
    color: var(--ink);
  }
  .spread {
    position: absolute; left: 40px; top: 46px;
    width: 1120px; height: 740px;
    display: flex;
    box-shadow: 0 10px 30px rgba(0,0,0,.18);
  }
  .panel { position: relative; width: 560px; height: 740px; overflow: hidden; }

  /* Back panel */
  .back-panel { background: var(--paper); }
  .block { position: absolute; background: var(--navy); }
  .block--top { left: 340px; top: 0; width: 220px; height: 270px; }
  .block--bottom { left: 400px; top: 560px; width: 160px; height: 180px; }
  .dashed-frame {
    position: absolute; left: 70px; top: 150px; width: 490px; height: 550px;
    border: 2px dashed var(--accent-red); border-right: none;
  }
  .section-tab {
    position: absolute; left: 0; top: 170px; width: 54px; height: 170px;
    background: var(--navy);
    display: flex; align-items: center; justify-content: center;
  }
  .section-tab span {
    transform: rotate(-90deg);
    color: var(--paper); font-weight: 800; font-size: 17px; letter-spacing: 2px;
    white-space: nowrap;
  }
  .locations { position: absolute; left: 90px; top: 180px; width: 240px; }
  .location { display: flex; gap: 10px; margin-bottom: 22px; }
  .location svg { flex: none; margin-top: 2px; }
  .location h3 { font-size: 12px; font-weight: 600; color: var(--accent-blue); margin-bottom: 3px; }
  .location p { font-size: 11px; line-height: 1.45; }
  .map-area {
    position: absolute; left: 110px; top: 330px; width: 320px; height: 290px;
    background: linear-gradient(160deg, #f4f5f7, #e4e6ea);
    border-radius: 6px;
  }

  /* Front cover */
  .cover { background: var(--navy-deep); }
  .cover-photo {
    position: absolute; inset: 0 0 200px 0;
    background: linear-gradient(150deg, var(--glass-light) 0%, var(--glass-mid) 40%, var(--glass-dark) 75%, var(--navy-deep) 100%);
  }
  .cover-title {
    position: absolute; right: 40px; top: 60px; text-align: right;
    color: var(--paper);
  }
  .cover-title h1 { font-size: 22px; font-weight: 800; letter-spacing: .5px; }
  .cover-title p { font-size: 15px; font-weight: 600; margin-top: 4px; opacity: .9; }
  .cover-band {
    position: absolute; left: 0; right: 0; bottom: 0; height: 200px;
    background: var(--navy);
  }
  .brand {
    position: absolute; left: 60px; top: 70px;
    display: flex; align-items: center; gap: 12px;
  }
  .brand-square { width: 22px; height: 22px; background: var(--accent-red); }
  .brand-name { color: var(--paper); font-weight: 800; font-size: 22px; }
  .brand-rule {
    position: absolute; left: 60px; top: 112px; width: 300px; height: 2px;
    background: var(--accent-red);
  }
</style>
</head>
<body>
  <main class="spread">
    <section class="panel back-panel">
      <div class="block block--top"></div>
      <div class="block block--bottom"></div>
      <div class="dashed-frame"></div>
      <div class="section-tab"><span>LOCATIONS</span></div>

      <div class="locations">
        <div class="location">
          <svg width="14" height="18" viewBox="0 0 14 18"><path d="M7 0C3 0 0 3 0 7c0 5 7 11 7 11s7-6 7-11c0-4-3-7-7-7z" fill="var(--accent-blue)"/><circle cx="7" cy="7" r="2.5" fill="#fff"/></svg>
          <div>
            <h3>Head Office</h3>
            <p>120 Harbor Road, Suite 4<br>Linden, NJ 07036<br>Tel: (908) 555-0142</p>
          </div>
        </div>
        <div class="location">
          <svg width="14" height="18" viewBox="0 0 14 18"><path d="M7 0C3 0 0 3 0 7c0 5 7 11 7 11s7-6 7-11c0-4-3-7-7-7z" fill="var(--ink)"/><circle cx="7" cy="7" r="2.5" fill="#fff"/></svg>
          <div>
            <h3>Plants &amp; Warehouses</h3>
            <p>Ohio · 44 Mill Street<br>Illinois · 9 Dock Lane<br>Virginia · 310 Rail Avenue</p>
          </div>
        </div>
      </div>

      <div class="map-area" role="img" aria-label="Outline map of the United States with pins marking company locations"></div>
    </section>

    <section class="panel cover">
      <div class="cover-photo" role="img" aria-label="Upward view of a glass office tower against a blue sky"></div>
      <div class="cover-title">
        <h1>Product Line Catalogue</h1>
        <p>Specialty Chemicals</p>
      </div>
      <div class="cover-band">
        <div class="brand">
          <span class="brand-square"></span>
          <span class="brand-name">Northgate Polymer, Inc.</span>
        </div>
        <div class="brand-rule"></div>
      </div>
    </section>
  </main>
</body>
</html>
```